Duel Business card

Want an edgy business card that shows both of our companies on each side of the card, OR both together with a cool design.

*Must be edgy: We have attached our two business logos. We are a bail bond and immigration bond company.

Would like the address on one side only.
Need Phone, cell, website, address, and Name

Company Name 1: Liberty Release Partners
www.libertyreleasepartners-example.com

Company Name 2: Crossway Custody Advocates
www.crosswaycustodyadvocates-example.com

These cards will need to be easily changeable so I can modify new employees

Target Market(s)

people in jail, takign imigrants out of jail and from being taken back to there country

Industry/Entity Type

Business

Requirements
Must have
• Include both logos attached

```html
<!DOCTYPE html>
<html lang="en">
<head>
<meta charset="utf-8">
<title>Dual Business Card – Liberty Release Partners &amp; Crossway Custody Advocates</title>
<link rel="stylesheet" href="https://fonts.googleapis.com/css2?family=Arimo:wght@400;700&display=swap">
<style>
  :root {
    --navy: #1c4066;
    --brand-blue: #1f3f8f;
    --gold: #f0c332;
    --red: #e0463f;
    --grey: #a7a7a7;
    --ink: #3a3a3a;
    --white: #ffffff;
    --page: #ffffff;
  }
  * { box-sizing: border-box; margin: 0; padding: 0; }
  html, body {
    width: 1200px; height: 900px; overflow: hidden;
    background: var(--page);
    font-family: "Arimo", Arial, sans-serif;
  }
  .canvas { position: relative; width: 1200px; height: 900px; }
  .card {
    position: absolute; left: 293px; width: 616px; height: 354px;
    background: var(--white);
    border: 1px solid #ececec;
    overflow: hidden;
  }
  .card--front { top: 67px; }
  .card--back { top: 477px; }

  /* Front */
  .front-brands {
    position: absolute; left: 0; top: 0; width: 295px; height: 100%;
    display: flex; flex-direction: column; align-items: center; justify-content: center; gap: 34px;
  }
  .brand-divider { position: absolute; left: 295px; top: 0; width: 11px; height: 100%; background: var(--grey); }
  .front-panel { position: absolute; left: 306px; top: 0; right: 0; height: 100%; background: var(--navy); }
  .name-band {
    position: absolute; left: 277px; top: 125px; width: 337px; height: 35px;
    background: var(--gold);
  }
  .person-name {
    position: absolute; left: 360px; top: 130px;
    color: var(--white); font-weight: 700; font-size: 20px; line-height: 26px;
  }
  .person-title {
    position: absolute; left: 360px; top: 165px;
    color: var(--white); font-size: 16px;
  }
  .contact {
    position: absolute; left: 360px; top: 226px;
    color: var(--white); font-size: 16px; line-height: 21px; list-style: none;
  }
  .contact-line { display: flex; align-items: center; gap: 6px; }
  .contact-icon { width: 13px; height: 15px; flex: none; }

  /* Brand marks */
  .brand { display: flex; align-items: center; gap: 10px; }
  .brand-dot { width: 26px; height: 26px; border-radius: 50%; flex: none; }
  .brand-name { font-weight: 700; font-size: 18px; line-height: 21px; }
  .brand--crossway .brand-dot { background: var(--red); }
  .brand--crossway .brand-name { color: var(--red); }
  .brand--liberty .brand-dot { background: var(--gold); }
  .brand--liberty .brand-name { color: var(--brand-blue); }

  /* Back */
  .back-brands {
    position: absolute; left: 0; top: 0; width: 100%; height: 335px;
    display: flex;
  }
  .back-column {
    flex: 1; display: flex; flex-direction: column; align-items: center; justify-content: center;
    padding-top: 60px; gap: 28px;
  }
  .website { color: var(--ink); font-size: 13px; }
  .back-rule { position: absolute; bottom: 0; left: 0; width: 100%; height: 19px; display: flex; }
  .back-rule .rule-navy { width: 315px; background: var(--navy); }
  .back-rule .rule-grey { flex: 1; background: var(--grey); }
</style>
</head>
<body>
<main class="canvas">

  <section class="card card--front" aria-label="Card front">
    <div class="front-brands">
      <div class="brand brand--crossway">
        <span class="brand-dot"></span>
        <span class="brand-name">Crossway<br>Custody Advocates</span>
      </div>
      <div class="brand brand--liberty">
        <span class="brand-dot"></span>
        <span class="brand-name">Liberty<br>Release Partners</span>
      </div>
    </div>
    <div class="brand-divider"></div>
    <div class="front-panel"></div>
    <div class="name-band"></div>
    <h1 class="person-name">Daniel Whitford</h1>
    <p class="person-title">Founder &amp; CEO</p>
    <ul class="contact">
      <li>4415 Harbor Mill Road</li>
      <li>Fairbrook, VA 20199</li>
      <li class="contact-line">
        <svg class="contact-icon" viewBox="0 0 13 15" aria-hidden="true">
          <path d="M2 1 L5 1 L6 4 L4.5 5.5 Q6 9 8.5 10.5 L10 9 L12.5 10 L12.5 13 Q6 14 2 8 Q0.5 4 2 1 Z" fill="var(--gold)"/>
        </svg>
        <span>(555) 014-2380</span>
      </li>
      <li class="contact-line">
        <svg class="contact-icon" viewBox="0 0 13 15" aria-hidden="true">
          <rect x="3" y="1" width="7" height="13" rx="1.5" fill="var(--gold)"/>
          <rect x="4.3" y="3" width="4.4" height="6" fill="var(--navy)"/>
        </svg>
        <span>(555) 014-2380</span>
      </li>
    </ul>
  </section>

  <section class="card card--back" aria-label="Card back">
    <div class="back-brands">
      <div class="back-column">
        <div class="brand brand--crossway">
          <span class="brand-dot"></span>
          <span class="brand-name">Crossway<br>Custody Advocates</span>
        </div>
        <p class="website">www.crosswaycustodyadvocates-example.com</p>
      </div>
      <div class="back-column">
        <div class="brand brand--liberty">
          <span class="brand-dot"></span>
          <span class="brand-name">Liberty<br>Release Partners</span>
        </div>
        <p class="website">www.libertyreleasepartners-example.com</p>
      </div>
    </div>
    <div class="back-rule"><span class="rule-navy"></span><span class="rule-grey"></span></div>
  </section>

</main>
</body>
</html>
```